Corvane Project Services - Flyer

Project Breif:
I need a single page A4 Capability Statement, which will be used to market our services to prospective clients, both in print and via email PDF.
It needs to look professional and should incorporate the elements I have uploaded into files, these include:
Capability Statement Text
Corvane Services Company Logo
Additional Logo’s (Tools We Use)
Glimmer Bay Pics can be cut into the page
I have included examples of capability statements as a guide to what i am looking for.
Regards
Derek
Engineering Consulting

```html
<!DOCTYPE html>
<html lang="en">
<head>
<meta charset="utf-8">
<title>Corvane Project Services – Capability Statement</title>
<link rel="stylesheet" href="https://fonts.googleapis.com/css2?family=Open+Sans:wght@400;600;700&family=Oswald:wght@400;500&display=swap">
<style>
:root{
  --page-bg:#d9d9d9;
  --paper:#ffffff;
  --ink:#3c3c3c;
  --brand-blue:#2f6fb5;
  --panel-blue:rgba(88,118,160,.86);
  --tab-blue:#7fb3dd;
  --card-head:#8aaed3;
  --card-line:#cfd9e4;
  --band-top:#9cc6e8;
  --muted:#6a7480;
}
*{box-sizing:border-box;margin:0;padding:0}
html,body{width:804px;height:1200px;overflow:hidden}
body{background:var(--page-bg);font-family:"Open Sans",Arial,sans-serif;color:var(--ink)}
.flyer{position:absolute;left:0;top:32px;width:804px;height:1136px;background:var(--paper);overflow:hidden}

/* header */
.brand{position:absolute;left:30px;top:22px;width:200px;text-align:center}
.brand-mark{width:56px;height:56px;border-radius:50%;background:var(--brand-blue);margin:0 auto 8px}
.brand-name{font-family:"Open Sans",Arial,sans-serif;font-weight:700;font-size:14px;letter-spacing:.5px;color:#4a4a4a;line-height:1.25}
.contact{position:absolute;right:48px;top:48px;text-align:right;font-size:12px;line-height:18px;color:#333}
.contact .who{color:var(--brand-blue);font-weight:700;font-size:11px;margin-bottom:3px}
.contact svg{width:10px;height:10px;vertical-align:-1px;margin-right:6px;fill:var(--brand-blue)}

/* hero */
.hero{position:absolute;left:0;top:150px;width:804px;height:446px}
.hero-photo{position:absolute;inset:0;background:linear-gradient(100deg,#8a98a8 0%,#b9c3cd 45%,#e4e8ec 70%,#cdd3d9 100%)}
.hero-panel{position:absolute;left:0;top:0;width:804px;height:446px}
.headline{position:absolute;left:32px;top:42px;font-family:"Oswald",Arial,sans-serif;color:#fff;text-transform:uppercase;line-height:29px}
.headline .strong{font-size:28px;font-weight:500;display:block}
.headline .light{font-size:23px;font-weight:400;display:block}
.intro{position:absolute;left:34px;top:236px;width:440px;color:#f2f5f9;font-size:11.5px;line-height:14px}
.intro p{margin-bottom:6px}

/* services */
.services-tab{position:absolute;left:280px;top:598px;width:244px;height:42px;background:var(--tab-blue);color:#fff;font-family:"Oswald",Arial,sans-serif;font-size:22px;text-align:center;line-height:42px;letter-spacing:.5px}
.service{position:absolute;top:710px;height:236px;background:#fff;border-radius:8px;box-shadow:0 2px 8px rgba(0,0,0,.18)}
.service-icon{position:absolute;left:50%;top:-46px;width:50px;height:50px;margin-left:-25px;border-radius:50%;background:var(--card-head);display:flex;align-items:center;justify-content:center}
.service-icon svg{width:26px;height:26px;fill:#fff}
.service-title{height:38px;background:var(--card-head);border-radius:8px 8px 0 0;color:#fff;font-size:10.5px;font-weight:700;text-align:center;line-height:38px;text-transform:uppercase}
.service ul{list-style:none;padding:10px 12px 0 12px}
.service li{position:relative;padding-left:16px;font-size:10px;line-height:12px;margin-bottom:8px;color:#2f4f78;font-weight:600}
.service li::before{content:"";position:absolute;left:0;top:1px;width:9px;height:9px;border:1px solid #7d8a98;border-radius:50%}
.s-plan{left:26px;width:206px}
.s-risk{left:301px;width:209px}
.s-cost{left:570px;width:208px}

/* tools */
.tools{position:absolute;left:0;top:982px;width:804px;height:154px;border-top:4px solid var(--band-top);background:linear-gradient(#ffffff,#ececec 60%,#dedede)}
.tool{position:absolute;top:0;height:150px;display:flex;align-items:center;gap:8px;font-family:"Open Sans",Arial,sans-serif;font-weight:700;font-size:15px}
.tool .dot{width:14px;height:14px}
.t1{left:34px;color:#c8372d}
.t1 .dot{background:#c8372d}
.t2{left:212px;color:#2d8a3e}
.t2 .dot{background:#2d8a3e}
.t3{left:400px;color:#c8232c}
.t3 .dot{background:#c8232c;border-radius:50%}
.t3 span{display:block;line-height:20px}
.t4{left:620px;color:#2a7fb0}
.t4 .dot{background:#2a7fb0;border-radius:50%}
.t4 span{display:block;line-height:20px}
</style>
</head>
<body>
<main class="flyer">
  <header>
    <div class="brand">
      <div class="brand-mark"></div>
      <div class="brand-name">CORVANE PROJECT<br>SERVICES</div>
    </div>
    <div class="contact">
      <div class="who">DEREK HALLORAN (MANAGING DIRECTOR)</div>
      <div><svg viewBox="0 0 10 10"><rect x="0" y="2" width="10" height="7" rx="1"/></svg>info@corvaneservices.ie</div>
      <div><svg viewBox="0 0 10 10"><circle cx="5" cy="5" r="4.5"/></svg>www.corvaneservices.ie</div>
      <div><svg viewBox="0 0 10 10"><path d="M2 1l2 0 1 2-1 1c.6 1.3 1.7 2.4 3 3l1-1 2 1v2c-4.5 0-8-3.5-8-8z"/></svg>+353 (0)870 415 962</div>
    </div>
  </header>

  <section class="hero">
    <div class="hero-photo" role="img" aria-label="Stock photo of hands holding and reviewing paper documents at a desk"></div>
    <svg class="hero-panel" viewBox="0 0 804 446" aria-hidden="true">
      <polygon points="0,0 470,0 560,250 520,446 0,446" fill="rgba(88,118,160,.86)"/>
    </svg>
    <h1 class="headline">
      <span class="strong">Corvane Project</span>
      <span class="light">Services is a leading</span>
      <span class="strong">Project Control</span>
      <span class="light">Consultancy based in</span>
      <span class="strong">Co. Cork Ireland.</span>
    </h1>
    <div class="intro">
      <p>Corvane Project Services Ltd. is a leading project control consultancy based in Co Cork Ireland</p>
      <p>For over 20 years we have been helping our clients to deliver complex projects and programs throughout mainland Europe.</p>
      <p>We are passionate about empower organisations to achieve their objectives, on time and on budget.</p>
      <p>We are continually innovating, evolving and learning, utilize the latest industry tools and techniques to deliver real value to our clients.</p>
      <p>Our goal is to make successful project delivery more achievable and repeatable.</p>
    </div>
  </section>

  <div class="services-tab">CORE SERVICES:</div>

  <section class="service s-plan">
    <div class="service-icon"><svg viewBox="0 0 26 26"><rect x="3" y="4" width="20" height="13" rx="1"/><rect x="11" y="18" width="4" height="4"/><rect x="7" y="22" width="12" height="2"/></svg></div>
    <div class="service-title">Planning and Scheduling</div>
    <ul>
      <li>Tender Planning</li>
      <li>Interactive Planning/ Pull Planning</li>
      <li>EPCMV Planning &amp; Scheduling</li>
      <li>Schedule Earned Value Management</li>
      <li>Independent Schedule Quality Assessment</li>
      <li>Schedule Risk Analysis (Monte Carlo)</li>
      <li>Training</li>
    </ul>
  </section>

  <section class="service s-risk">
    <div class="service-icon"><svg viewBox="0 0 26 26"><circle cx="13" cy="6" r="3.5"/><circle cx="6" cy="16" r="3.5"/><circle cx="20" cy="16" r="3.5"/><rect x="2" y="21" width="8" height="3" rx="1"/><rect x="16" y="21" width="8" height="3" rx="1"/></svg></div>
    <div class="service-title">Management of Risk</div>
    <ul>
      <li>Risk Management Policies &amp; Procedures</li>
      <li>Risk Management Strategy</li>
      <li>Risk Registers</li>
      <li>Risk Improvement Planning</li>
      <li>Risk Response and Communication</li>
      <li>Risk Management Training</li>
    </ul>
  </section>

  <section class="service s-cost">
    <div class="service-icon"><svg viewBox="0 0 26 26"><rect x="3" y="15" width="4" height="8"/><rect x="9" y="11" width="4" height="12"/><rect x="15" y="13" width="4" height="10"/><rect x="21" y="8" width="3" height="15"/><polygon points="3,11 10,5 15,9 23,2 24,4 15,12 10,8 4,13"/></svg></div>
    <div class="service-title">Cost Control</div>
    <ul>
      <li>Estimating &amp; Forecasting</li>
      <li>Earned Value Analysis</li>
      <li>Progress Reporting</li>
      <li>Cost Risk Analysis</li>
    </ul>
  </section>

  <footer class="tools" aria-label="Tools we use">
    <div class="tool t1"><i class="dot"></i>Tessaline Planner</div>
    <div class="tool t2"><i class="dot"></i>Plotwell Schedule</div>
    <div class="tool t3"><i class="dot"></i><div><span>Vantor Powerplan</span><span>Markstone Pro</span></div></div>
    <div class="tool t4"><i class="dot"></i><div><span>RiskFrame</span><span>Quillon Analyzer</span></div></div>
  </footer>
</main>
</body>
</html>
```